" A empresa atua em dois segmentos: 1) atendimento psicológico de crianças, adolescentes e adultos e 2) recrutamento, seleçao e treinamento de pessoas. A proposta é trabalhar com o desenvolvimento humano em suas diversas dimensoes. "

```html
<!DOCTYPE html>
<html lang="pt-BR">
<head>
<meta charset="utf-8">
<title>Rumo Vivo — Cartão de visita</title>
<link rel="stylesheet" href="https://fonts.googleapis.com/css2?family=Open+Sans:wght@400;600&display=swap">
<style>
  :root {
    --teal: #17a39b;
    --ink-gray: #6d6e70;
    --card: #ffffff;
    --backdrop: #ececea;
    --on-teal: #ffffff;
  }
  * { box-sizing: border-box; margin: 0; padding: 0; }
  html, body {
    width: 1200px;
    height: 1200px;
    overflow: hidden;
    background: var(--backdrop);
    font-family: "Open Sans", Verdana, sans-serif;
  }
  .card {
    position: absolute;
    left: 235px;
    width: 760px;
    height: 420px;
    background: var(--card);
    border-radius: 24px;
    overflow: hidden;
    box-shadow: 0 2px 10px rgba(0,0,0,0.12);
  }
  .card--front { top: 163px; }
  .card--back { top: 636px; }

  .front-brand {
    position: absolute;
    inset: 0;
    display: flex;
    align-items: center;
    justify-content: center;
    gap: 34px;
  }
  .brand-dot {
    width: 190px;
    height: 190px;
    border-radius: 50%;
    background: var(--teal);
  }
  .brand-name {
    color: var(--teal);
    font-weight: 400;
    font-size: 64px;
    letter-spacing: 0.5px;
  }

  .back-panel {
    position: absolute;
    inset: 0;
    width: 100%;
    height: 100%;
  }
  .contact {
    position: absolute;
    left: 46px;
    top: 0;
    color: var(--on-teal);
  }
  .contact__name {
    position: absolute;
    top: 42px;
    white-space: nowrap;
    font-size: 34px;
    font-weight: 400;
    letter-spacing: 1px;
  }
  .contact__role {
    position: absolute;
    top: 86px;
    font-size: 22px;
  }
  .contact__email {
    position: absolute;
    top: 124px;
    white-space: nowrap;
    font-size: 22px;
  }
  .contact__details {
    position: absolute;
    top: 242px;
    list-style: none;
    font-size: 21px;
    line-height: 31px;
    white-space: nowrap;
  }
  .back-brand {
    position: absolute;
    left: 375px;
    top: 298px;
    display: flex;
    align-items: center;
    gap: 20px;
  }
  .back-brand .brand-dot {
    width: 76px;
    height: 76px;
  }
  .back-brand .brand-name {
    font-size: 48px;
  }
</style>
</head>
<body>
  <section class="card card--front" aria-label="Frente do cartão">
    <div class="front-brand">
      <span class="brand-dot"></span>
      <span class="brand-name">Rumo Vivo</span>
    </div>
  </section>

  <section class="card card--back" aria-label="Verso do cartão">
    <svg class="back-panel" viewBox="0 0 760 420" preserveAspectRatio="none" aria-hidden="true">
      <polygon points="0,0 461,0 329,420 0,420" fill="var(--teal)"/>
    </svg>
    <div class="contact">
      <h1 class="contact__name">Marina Tavares</h1>
      <p class="contact__role">cargo</p>
      <p class="contact__email">marina@rumovivo.com.br</p>
      <ul class="contact__details">
        <li>Rua das Acácias n°215</li>
        <li>Campinas&nbsp; S.P.</li>
        <li>19 3412-7788</li>
        <li>19 99827-4410</li>
        <li>www.rumovivo.com.br</li>
      </ul>
    </div>
    <div class="back-brand">
      <span class="brand-dot"></span>
      <span class="brand-name">Rumo Vivo</span>
    </div>
  </section>
</body>
</html>
```